Sheriff Candidate needs a large yard sign

A candidate for Sheriff needs to have a sign to put in front of businesses and houses that advertise her candidacy.

Target Market(s)

Democrats, voters

Industry/Entity Type

Political

Font styles to use
Sans Serif

Colors
34a7d7
3276b5

Requirements
Must have
• Must have her picture
• Must have the words "Elect Dana Holloway" - I'd like the name Dana to be smaller Holloway. "Elect" and "Holloway" should be the focus.
• at the bottom in a box "Paid for by the Committee to Elect Dana Holloway"
Nice to have
• it would be good to have her logo as well.
• blue color for democrats and on a white background
Should not have
• pink color

```html
<!DOCTYPE html>
<html lang="en">
<head>
<meta charset="utf-8">
<title>Elect Dana Holloway – Yard Sign</title>
<link href="https://fonts.googleapis.com/css2?family=Old+Standard+TT:ital,wght@0,400;0,700;1,400&display=swap" rel="stylesheet">
<style>
  :root {
    --backdrop: #626262;
    --sign-white: #ffffff;
    --blue-light: #34a7d7;
    --blue-dark: #3276b5;
    --gold: #c9a23a;
    --navy: #1d2a44;
    --photo-top: #8a8583;
    --photo-bottom: #2a2d38;
  }
  * { margin: 0; padding: 0; box-sizing: border-box; }
  html, body {
    width: 1200px; height: 888px; overflow: hidden;
    background: var(--backdrop);
  }
  .yard-sign {
    position: absolute; left: 263px; top: 174px;
    width: 696px; height: 523px;
    background: var(--sign-white);
    font-family: "Old Standard TT", Georgia, serif;
  }
  .stripe { position: absolute; height: 26px; }
  .stripe-left { left: 0; top: 58px; width: 31px; background: var(--blue-light); }
  .stripe-center, .stripe-right {
    top: 58px;
    background: linear-gradient(var(--blue-light) 0 50%, var(--blue-dark) 50% 100%);
  }
  .stripe-center { left: 176px; width: 237px; }
  .stripe-right { left: 667px; width: 29px; }
  .campaign-mark {
    position: absolute; left: 46px; top: 19px;
    width: 112px; height: 112px; border-radius: 50%;
    background: var(--gold);
    display: flex; align-items: center; justify-content: center;
    text-align: center;
    font-weight: 700; font-size: 15px; line-height: 1.15;
    color: var(--navy);
  }
  .headline { position: absolute; left: 0; top: 0; color: var(--blue-dark); }
  .headline-elect {
    position: absolute; left: 39px; top: 160px;
    font-size: 94px; font-weight: 700; line-height: 1;
    color: var(--blue-dark); letter-spacing: -1px;
  }
  .headline-first {
    position: absolute; left: 64px; top: 244px;
    font-size: 50px; font-style: italic; font-weight: 400; line-height: 1;
    color: var(--blue-light);
  }
  .headline-last {
    position: absolute; left: 90px; top: 287px;
    font-size: 78px; font-weight: 700; line-height: 1;
    color: var(--blue-dark); letter-spacing: -1.5px;
  }
  .candidate-photo {
    position: absolute; left: 420px; top: 27px;
    width: 240px; height: 343px;
    background: linear-gradient(180deg, var(--photo-top) 0%, #6f6b6b 45%, var(--photo-bottom) 100%);
  }
  .disclaimer-ribbon { position: absolute; left: 35px; top: 423px; width: 635px; height: 71px; }
  .disclaimer-ribbon svg { position: absolute; inset: 0; }
  .disclaimer-text {
    position: absolute; inset: 0;
    display: flex; align-items: center; justify-content: center;
    color: var(--sign-white); font-size: 24px; letter-spacing: 0.3px;
  }
</style>
</head>
<body>
  <main class="yard-sign">
    <div class="stripe stripe-left"></div>
    <div class="stripe stripe-center"></div>
    <div class="stripe stripe-right"></div>

    <div class="campaign-mark">Holloway<br>for<br>Sheriff</div>

    <h1 class="headline">
      <span class="headline-elect">Elect</span>
      <span class="headline-first">Dana</span>
      <span class="headline-last">Holloway</span>
    </h1>

    <div class="candidate-photo" role="img" aria-label="Portrait photo of the candidate in a dark blazer against a grey studio backdrop"></div>

    <div class="disclaimer-ribbon">
      <svg width="635" height="71" viewBox="0 0 635 71" aria-hidden="true">
        <polygon points="0,0 635,0 599,35.5 635,71 0,71 36,35.5" fill="var(--blue-dark)"/>
      </svg>
      <p class="disclaimer-text">Paid for by the Committee to Elect Dana Holloway</p>
    </div>
  </main>
</body>
</html>
```